Divorce Lawyer print and ebook cover (Planting gardens after every storm )

I need a front and back cover for my divorce and family law book. I already have a photo and title. The back cover photo is not necessary but can be interesting the Front-main cover is a must

Target Market(s)

Prospective client

Colors

Designer to choose colors to be used in the design.

Requirements
Must have
• Front photo by viewable.

```html
<!DOCTYPE html>
<html lang="en">
<head>
<meta charset="utf-8">
<title>Planting gardens after every storm – cover</title>
<link rel="stylesheet" href="https://fonts.googleapis.com/css2?family=Bebas+Neue&family=Amatic+SC:wght@700&display=swap">
<style>
  :root {
    --ink: #0d0d0d;
    --ink-soft: #1b1b1b;
    --rust: #a84a14;
    --rust-bright: #d1581a;
    --paper: #ffffff;
    --backdrop: #e9eeee;
    --photo-light: #cfcfcf;
    --photo-dark: #3a3a3a;
  }
  * { margin: 0; padding: 0; box-sizing: border-box; }
  html, body { width: 684px; height: 1200px; overflow: hidden; }
  body { background: var(--backdrop); position: relative; }

  .cover-wrap {
    position: absolute;
    left: 19px; top: 372px;
    width: 646px; height: 456px;
    display: flex;
  }

  .back-cover {
    width: 304px; height: 100%;
    background: radial-gradient(ellipse at 40% 45%, var(--ink-soft) 0%, var(--ink) 70%);
  }

  .spine {
    width: 38px; height: 100%;
    background: var(--rust);
    display: flex; align-items: center; justify-content: center;
  }
  .spine-title {
    writing-mode: vertical-rl;
    white-space: nowrap;
    line-height: 1;
    padding-top: 40px;
  }
  .spine-title .main { font-family: "Bebas Neue", sans-serif; font-size: 26px; color: var(--ink); letter-spacing: 0.5px; }
  .spine-title .sub { font-family: "Amatic SC", cursive; font-size: 24px; color: var(--paper); margin-top: 8px; }

  .front-cover {
    position: relative;
    width: 304px; height: 100%;
    background: var(--ink);
    overflow: hidden;
  }
  .front-bands { position: absolute; inset: 0; }
  .front-photo {
    position: absolute; inset: 0;
    background: linear-gradient(160deg, var(--photo-light) 0%, #8f8f8f 45%, var(--photo-dark) 100%);
    clip-path: polygon(0 138px, 100% 126px, 100% 334px, 0 356px);
  }
  .front-title {
    position: absolute;
    left: 12px; right: 8px; top: 34px;
    line-height: 0.9;
  }
  .front-title .main {
    display: block;
    font-family: "Bebas Neue", sans-serif;
    font-size: 45px;
    color: var(--rust-bright);
    letter-spacing: 0.5px;
  }
  .front-title .sub {
    display: block;
    font-family: "Amatic SC", cursive;
    font-size: 40px;
    color: var(--paper);
    margin-top: 4px;
  }
</style>
</head>
<body>
  <div class="cover-wrap">
    <div class="back-cover"></div>

    <div class="spine">
      <div class="spine-title">
        <span class="main">PLANTING GARDENS</span>
        <span class="sub">AFTER EVERY STORM</span>
      </div>
    </div>

    <div class="front-cover">
      <svg class="front-bands" width="304" height="456" viewBox="0 0 304 456">
        <polygon points="0,128 304,116 304,126 0,138" fill="var(--rust)"/>
        <polygon points="0,356 304,334 304,344 0,366" fill="var(--rust)"/>
      </svg>
      <div class="front-photo" role="img" aria-label="Black and white photo of a toddler in a knitted hat on a park swing, held by two adults' hands"></div>
      <h1 class="front-title">
        <span class="main">PLANTING GARDENS</span>
        <span class="sub">AFTER EVERY STORM</span>
      </h1>
    </div>
  </div>
</body>
</html>
```